Project VOIP Phone

Lumerix Antilles needs a advertisement design for a new product called a VOIP PHONE. A VOIP Phone stands for Voice Over Internet Protocol. The advantages in comparison with a PSTN (Packet-Switched Telephone Network) are that a VOIP system saves a lot of money. Besides that it is simple, flexible and is the future of telecom.
The text of the advertisement should be:
' Get your VOIP PHONE SYSTEM starting at ƒ 25,- per phone (p/m)'
'VOIP PHONE SYSTEM' and 'ƒ 25,-' should be bigger than the rest, '(p/m)' should be smaller than the rest.
Under that our contact data should follow:
Lumerix Antilles
Tel: +599 9 732-1184
E-mail: sales@lumerix-demo.cw
Website: www.lumerix-demo.cw
The last rule of the Banner must contain a small text:
''Lumerix Cloud Solotions & Management''
We want to receive an optional design with some watermarks in the back with 2 or 3 words like: "cheap'' ''solid'' or ''reliable'' ''up coming'' ''Future'' or something like that.
We also want some pictures (attached) in the banner. Not al the pictures are needed, just whatever looks best on it.
The banner must have a size of: 728x200.
Good luck!
Updates
Please help us with this interesting project in the future of telephony

```html
<!DOCTYPE html>
<html lang="en">
<head>
<meta charset="utf-8">
<title>Lumerix Antilles – VoIP Phone System Banner</title>
<link rel="stylesheet" href="https://fonts.googleapis.com/css2?family=Arimo:ital,wght@0,400;0,700;1,700&family=Mulish:wght@400;800&display=swap">
<style>
  :root {
    --stage-light: #ffffff;
    --stage-dark: #dedede;
    --sky-light: #84cdf2;
    --sky-mid: #3fb3ea;
    --sky-deep: #0c9bdc;
    --price-stroke: #1a8ccc;
    --divider-grey: #d6d6d6;
    --card-white: #f3f3f3;
    --ink: #262626;
    --brand-blue: #1f9ad6;
    --watermark: rgba(255, 255, 255, 0.13);
  }
  html, body {
    margin: 0;
    padding: 0;
    width: 1200px;
    height: 1200px;
    overflow: hidden;
  }
  body {
    background: radial-gradient(circle at 50% 50%, var(--stage-light) 0%, var(--stage-light) 38%, var(--stage-dark) 100%);
  }
  .banner {
    position: absolute;
    left: 66px;
    top: 454px;
    width: 1065px;
    height: 291px;
    display: block;
  }
  .headline { font-family: "Arimo", Arial, sans-serif; fill: #ffffff; }
  .headline-light { font-weight: 400; }
  .headline-strong { font-weight: 700; }
  .price-figure {
    font-family: "Arimo", Arial, sans-serif;
    font-weight: 700;
    fill: #ffffff;
    stroke: var(--price-stroke);
    stroke-width: 2.5;
    paint-order: stroke;
  }
  .price-symbol { font-style: italic; }
  .watermark-word {
    font-family: "Arimo", Arial, sans-serif;
    font-weight: 700;
    fill: var(--watermark);
  }
  .brand-name {
    font-family: "Mulish", Arial, sans-serif;
    font-weight: 800;
    fill: var(--brand-blue);
  }
  .contact-line {
    font-family: "Mulish", Arial, sans-serif;
    font-weight: 400;
    fill: var(--ink);
  }
</style>
</head>
<body>
<svg class="banner" viewBox="0 0 1065 291" xmlns="http://www.w3.org/2000/svg">
  <defs>
    <linearGradient id="sky-panel" x1="0" y1="0" x2="1" y2="0">
      <stop offset="0" stop-color="var(--sky-light)"/>
      <stop offset="0.45" stop-color="var(--sky-light)"/>
      <stop offset="0.75" stop-color="var(--sky-mid)"/>
      <stop offset="1" stop-color="var(--sky-deep)"/>
    </linearGradient>
    <linearGradient id="voip-art" x1="0" y1="0" x2="1" y2="1">
      <stop offset="0" stop-color="#b9e4f7"/>
      <stop offset="1" stop-color="#4aa6c9"/>
    </linearGradient>
  </defs>

  <!-- contact card background -->
  <rect class="contact-card" x="0" y="0" width="1065" height="291" fill="var(--card-white)"/>

  <!-- grey divider curve -->
  <path class="divider-curve" d="M697,0 H717 Q792,145 730,291 H711 Q770,145 697,0 Z" fill="var(--divider-grey)"/>

  <!-- blue offer panel -->
  <path class="offer-panel" d="M0,0 H697 Q770,145 711,291 H0 Z" fill="url(#sky-panel)"/>

  <!-- faint background words -->
  <g class="watermarks">
    <text class="watermark-word" x="35" y="160" font-size="70">CLOUD</text>
    <text class="watermark-word" x="270" y="175" font-size="34">SOLID</text>
    <text class="watermark-word" x="290" y="225" font-size="34">FUTURE</text>
    <text class="watermark-word" x="505" y="142" font-size="26">UP COMING</text>
  </g>

  <!-- VoIP lettering with handset artwork -->
  <rect class="voip-artwork" x="71" y="37" width="206" height="160" rx="14" fill="url(#voip-art)" opacity="0.85"
        role="img" aria-label="Glossy 3D VoIP lettering with a coiled telephone handset"/>

  <!-- offer copy -->
  <text class="headline headline-light" x="259" y="48" font-size="25">Get your</text>
  <text class="headline headline-strong" x="295" y="113" font-size="34">PHONE SYSTEM</text>
  <text class="headline headline-light" x="262" y="198" font-size="23">starting</text>
  <text class="headline headline-light" x="322" y="230" font-size="23">at</text>

  <text class="price-figure price-symbol" x="346" y="252" font-size="158">ƒ</text>
  <text class="price-figure" x="400" y="232" font-size="140" letter-spacing="-4">25</text>

  <text class="headline headline-light" x="400" y="262" font-size="23">per phone <tspan font-size="21">(p/m)</tspan></text>

  <!-- brand block -->
  <g class="brand">
    <rect class="brand-mark" x="913" y="26" width="84" height="80" rx="6" fill="var(--brand-blue)"/>
    <text class="brand-name" x="955" y="138" font-size="24" text-anchor="middle">Lumerix</text>
  </g>

  <!-- contact details -->
  <g class="contact-details" text-anchor="end">
    <text class="contact-line" x="1034" y="188" font-size="19">Lumerix Antilles</text>
    <text class="contact-line" x="1034" y="214" font-size="19">Tel: +599 9 732-1184</text>
    <text class="contact-line" x="1034" y="240" font-size="19">E-mail: sales@lumerix-demo.cw</text>
    <text class="contact-line" x="1034" y="266" font-size="19">Website: www.lumerix-demo.cw</text>
  </g>
</svg>
</body>
</html>
```